Redesign of existing Vantix app (no coding)

I want a redesign (design only - no coding) of this Vantix app http://qrv.zx/7t3KpRv

The features will remain the same but I need a fresh/different layout (including navigation) and the colour scheme should be based on ec018c/ RGB: 236,1,140

Screens required to choose the winner who will then design all the screens:

- Search screens (in the current app there are various search scenarios - I need to see them all whether they are integrated in 1 screen or not)
- Navigation (main tab bar and More menu)
- Restaurant search results
- Restaurant details screen

```html
<!DOCTYPE html>
<html lang="en">
<head>
<meta charset="utf-8">
<title>All Restaurants</title>
<link rel="stylesheet" href="https://fonts.googleapis.com/css2?family=Roboto+Condensed:wght@700&family=Signika:wght@300;400;500&display=swap">
<style>
:root{
  --pink:#ec018c;
  --plum:#a0005f;
  --plum-deep:#9a0058;
  --wine:#6b0039;
  --ink:#1c222c;
  --card:#f2f2f2;
  --rule:#dcdcdc;
  --divider:#e0e0e0;
  --text:#5a5e64;
  --muted:#b0b3b7;
  --white:#ffffff;
  --dot-soft:#e48bbf;
}
*{margin:0;padding:0;box-sizing:border-box}
html,body{width:676px;height:1200px;overflow:hidden;background:var(--ink)}
.app{position:relative;width:676px;height:1200px;background:var(--ink);font-family:"Signika",sans-serif}

.status-bar{height:42px;background:var(--plum);color:var(--white);display:flex;align-items:center;justify-content:space-between;padding:0 12px;font-size:22px}
.status-bar .time{font-weight:500;font-size:24px}
.status-bar .left,.status-bar .right{display:flex;align-items:center;gap:8px}
.dots{display:flex;gap:3px}
.dots i{width:11px;height:11px;border-radius:50%;background:var(--white);display:block}
.dots i.off{background:none;border:1px solid var(--white)}
.battery{width:40px;height:18px;border:2px solid var(--white);border-radius:4px;padding:2px}
.battery b{display:block;height:100%;background:var(--white);border-radius:1px}

.top-bar{height:116px;background:var(--pink);display:flex;align-items:center}
.top-bar .back{width:170px;height:100%;display:flex;align-items:center;justify-content:center;border-right:1px solid rgba(0,0,0,.08)}
.top-bar h1{flex:1;text-align:center;font-family:"Roboto Condensed",sans-serif;font-weight:700;font-size:31px;color:var(--wine);letter-spacing:.3px}
.top-bar .sort{width:155px;height:100%;display:flex;align-items:center;justify-content:center;border-left:1px solid rgba(0,0,0,.08)}

.list{position:absolute;top:162px;left:5px;width:666px}
.card{position:relative;display:flex;height:182px;margin-bottom:3px;background:var(--card);border-bottom:3px solid var(--rule);overflow:hidden}
.photo{width:184px;height:100%;flex:none}
.p1{background:linear-gradient(160deg,#c9d8ea,#4c8fd3 55%,#1e3f73)}
.p2{background:linear-gradient(160deg,#9c7a4e,#d8b98a 45%,#6fc5c9 75%,#5a4a33)}
.p3{background:linear-gradient(160deg,#7a3b9a,#cfa0d6 45%,#e8e0ea 70%,#8e7a5a)}
.p4{background:linear-gradient(180deg,#3b62b8,#c8d2dc 55%,#3fa0c8)}
.p5{background:linear-gradient(180deg,#0e1a3e,#7d5a2a 50%,#e0a24a 80%,#4a2a12)}

.info{flex:1;padding:24px 0 0 34px;position:relative}
.name{font-size:24px;font-weight:400;color:var(--text);line-height:28px}
.address{margin-top:6px;font-size:23px;font-weight:300;line-height:23px;color:var(--muted);width:380px}
.actions{position:absolute;left:26px;right:0;bottom:14px;display:flex;align-items:center;height:42px}
.action{display:flex;align-items:center;gap:12px;font-size:19px;font-weight:300;color:var(--muted);padding-right:32px;border-right:2px solid var(--divider);height:100%}
.action.map{padding-left:26px;padding-right:40px}
.action.fav{border:none;padding:0 0 0 22px}

.score{position:absolute;top:0;right:0;width:80px;height:80px}
.score span{position:absolute;top:10px;right:6px;color:var(--white);font-size:19px}

.tab-bar{position:absolute;left:5px;right:5px;top:1086px;height:108px;display:flex}
.tab{display:flex;flex-direction:column;align-items:center;justify-content:center;gap:8px;color:var(--white);font-family:"Roboto Condensed",sans-serif;font-weight:700;font-size:22px}
.tab.profile{width:211px;background:var(--plum-deep)}
.tab.home{flex:1;background:var(--ink)}
.tab.more{width:230px;background:var(--plum-deep)}
</style>
</head>
<body>
<div class="app">
  <div class="status-bar">
    <div class="left">
      <span class="dots"><i></i><i></i><i></i><i></i><i class="off"></i></span>
      <span>Carrier</span>
      <svg width="22" height="18" viewBox="0 0 22 18"><path d="M11 17l3-4a5 5 0 0 0-6 0zM4 9a10 10 0 0 1 14 0l2-2a13 13 0 0 0-18 0z" fill="#fff"/></svg>
    </div>
    <span class="time">12:34 AM</span>
    <div class="right">
      <svg width="16" height="18" viewBox="0 0 16 18"><path d="M15 1L1 8h7v9z" fill="#fff"/></svg>
      <span>100%</span>
      <span class="battery"><b></b></span>
    </div>
  </div>

  <header class="top-bar">
    <div class="back"><svg width="30" height="44" viewBox="0 0 30 44"><path d="M24 4L6 22l18 18" stroke="#6b0039" stroke-width="6" fill="none"/></svg></div>
    <h1>ALL RESTAURANTS</h1>
    <div class="sort">
      <svg width="90" height="52" viewBox="0 0 90 52"><rect x="3" y="3" width="44" height="44" rx="8" fill="none" stroke="#6b0039" stroke-width="6"/><g fill="#6b0039"><rect x="12" y="13" width="5" height="5"/><rect x="21" y="13" width="17" height="5"/><rect x="12" y="23" width="5" height="5"/><rect x="21" y="23" width="17" height="5"/><rect x="12" y="33" width="5" height="5"/><rect x="21" y="33" width="17" height="5"/></g><path d="M70 6v38M57 31l13 13 13-13" stroke="#6b0039" stroke-width="6" fill="none"/></svg>
    </div>
  </header>

  <main class="list">
    <article class="card">
      <div class="photo p1" role="img" aria-label="Hotel pool terrace with white buildings at dusk"></div>
      <div class="info">
        <h2 class="name">The Lantern</h2>
        <p class="address">4 The Arcade , Harbour Street, Marlow Bayfront Vellora</p>
        <div class="actions">
          <span class="action"><svg width="18" height="30" viewBox="0 0 18 30"><rect x="1.5" y="1.5" width="15" height="27" rx="3" fill="none" stroke="#1c222c" stroke-width="3"/><rect x="5" y="24" width="8" height="2" fill="#1c222c"/></svg>5550192837</span>
          <span class="action map"><svg width="22" height="30" viewBox="0 0 22 30"><path d="M11 0a11 11 0 0 0-11 11c0 8 11 19 11 19s11-11 11-19A11 11 0 0 0 11 0zm0 15a4 4 0 1 1 0-8 4 4 0 0 1 0 8z" fill="#1c222c"/></svg>Find it on map</span>
          <span class="action fav"><svg width="32" height="32" viewBox="0 0 32 32"><circle cx="16" cy="16" r="14" fill="none" stroke="#1c222c" stroke-width="3"/><path d="M16 7l2.6 5.6 6 .6-4.5 4 1.3 6-5.4-3.1-5.4 3.1 1.3-6-4.5-4 6-.6z" fill="#1c222c"/></svg></span>
        </div>
      </div>
      <div class="score"><svg width="80" height="80" viewBox="0 0 80 80"><path d="M0 0h80v80z" fill="#6b0039"/></svg><span>10.0</span></div>
    </article>

    <article class="card">
      <div class="photo p2" role="img" aria-label="Courtyard plunge pool with palm trees at evening"></div>
      <div class="info">
        <h2 class="name">The Lantern</h2>
        <p class="address">4 The Arcade , Harbour Street, Marlow Bayfront Vellora</p>
        <div class="actions">
          <span class="action"><svg width="18" height="30" viewBox="0 0 18 30"><rect x="1.5" y="1.5" width="15" height="27" rx="3" fill="none" stroke="#1c222c" stroke-width="3"/><rect x="5" y="24" width="8" height="2" fill="#1c222c"/></svg>5550192837</span>
          <span class="action map"><svg width="22" height="30" viewBox="0 0 22 30"><path d="M11 0a11 11 0 0 0-11 11c0 8 11 19 11 19s11-11 11-19A11 11 0 0 0 11 0zm0 15a4 4 0 1 1 0-8 4 4 0 0 1 0 8z" fill="#1c222c"/></svg>Find it on map</span>
          <span class="action fav"><svg width="32" height="32" viewBox="0 0 32 32"><circle cx="16" cy="16" r="14" fill="none" stroke="#1c222c" stroke-width="3"/><path d="M16 7l2.6 5.6 6 .6-4.5 4 1.3 6-5.4-3.1-5.4 3.1 1.3-6-4.5-4 6-.6z" fill="#1c222c"/></svg></span>
        </div>
      </div>
      <div class="score"><svg width="80" height="80" viewBox="0 0 80 80"><path d="M0 0h80v80z" fill="#6b0039"/></svg><span>10.0</span></div>
    </article>

    <article class="card">
      <div class="photo p3" role="img" aria-label="Lounge interior with white chairs under purple light"></div>
      <div class="info">
        <h2 class="name">The Lantern</h2>
        <p class="address">4 The Arcade , Harbour Street, Marlow Bayfront Vellora</p>
        <div class="actions">
          <span class="action"><svg width="18" height="30" viewBox="0 0 18 30"><rect x="1.5" y="1.5" width="15" height="27" rx="3" fill="none" stroke="#1c222c" stroke-width="3"/><rect x="5" y="24" width="8" height="2" fill="#1c222c"/></svg>5550192837</span>
          <span class="action map"><svg width="22" height="30" viewBox="0 0 22 30"><path d="M11 0a11 11 0 0 0-11 11c0 8 11 19 11 19s11-11 11-19A11 11 0 0 0 11 0zm0 15a4 4 0 1 1 0-8 4 4 0 0 1 0 8z" fill="#1c222c"/></svg>Find it on map</span>
          <span class="action fav"><svg width="32" height="32" viewBox="0 0 32 32"><circle cx="16" cy="16" r="14" fill="none" stroke="#1c222c" stroke-width="3"/><path d="M16 7l2.6 5.6 6 .6-4.5 4 1.3 6-5.4-3.1-5.4 3.1 1.3-6-4.5-4 6-.6z" fill="#1c222c"/></svg></span>
        </div>
      </div>
      <div class="score"><svg width="80" height="80" viewBox="0 0 80 80"><path d="M0 0h80v80z" fill="#6b0039"/></svg><span>10.0</span></div>
    </article>

    <article class="card">
      <div class="photo p4" role="img" aria-label="White seaside hotel with pool and palm trees"></div>
      <div class="info">
        <h2 class="name">The Lantern</h2>
        <p class="address">4 The Arcade , Harbour Street, Marlow Bayfront Vellora</p>
        <div class="actions">
          <span class="action"><svg width="18" height="30" viewBox="0 0 18 30"><rect x="1.5" y="1.5" width="15" height="27" rx="3" fill="none" stroke="#1c222c" stroke-width="3"/><rect x="5" y="24" width="8" height="2" fill="#1c222c"/></svg>5550192837</span>
          <span class="action map"><svg width="22" height="30" viewBox="0 0 22 30"><path d="M11 0a11 11 0 0 0-11 11c0 8 11 19 11 19s11-11 11-19A11 11 0 0 0 11 0zm0 15a4 4 0 1 1 0-8 4 4 0 0 1 0 8z" fill="#1c222c"/></svg>Find it on map</span>
          <span class="action fav"><svg width="32" height="32" viewBox="0 0 32 32"><circle cx="16" cy="16" r="14" fill="none" stroke="#1c222c" stroke-width="3"/><path d="M16 7l2.6 5.6 6 .6-4.5 4 1.3 6-5.4-3.1-5.4 3.1 1.3-6-4.5-4 6-.6z" fill="#1c222c"/></svg></span>
        </div>
      </div>
      <div class="score"><svg width="80" height="80" viewBox="0 0 80 80"><path d="M0 0h80v80z" fill="#6b0039"/></svg><span>10.0</span></div>
    </article>

    <article class="card">
      <div class="photo p5" role="img" aria-label="Lit hotel tower at night"></div>
      <div class="info">
        <h2 class="name">The Lantern</h2>
        <p class="address">4 The Arcade , Harbour Street, Marlow Bayfront Vellora</p>
        <div class="actions">
          <span class="action"><svg width="18" height="30" viewBox="0 0 18 30"><rect x="1.5" y="1.5" width="15" height="27" rx="3" fill="none" stroke="#1c222c" stroke-width="3"/><rect x="5" y="24" width="8" height="2" fill="#1c222c"/></svg>5550192837</span>
          <span class="action map"><svg width="22" height="30" viewBox="0 0 22 30"><path d="M11 0a11 11 0 0 0-11 11c0 8 11 19 11 19s11-11 11-19A11 11 0 0 0 11 0zm0 15a4 4 0 1 1 0-8 4 4 0 0 1 0 8z" fill="#1c222c"/></svg>Find it on map</span>
          <span class="action fav"><svg width="32" height="32" viewBox="0 0 32 32"><circle cx="16" cy="16" r="14" fill="none" stroke="#1c222c" stroke-width="3"/><path d="M16 7l2.6 5.6 6 .6-4.5 4 1.3 6-5.4-3.1-5.4 3.1 1.3-6-4.5-4 6-.6z" fill="#1c222c"/></svg></span>
        </div>
      </div>
      <div class="score"><svg width="80" height="80" viewBox="0 0 80 80"><path d="M0 0h80v80z" fill="#6b0039"/></svg><span>10.0</span></div>
    </article>
  </main>

  <nav class="tab-bar">
    <div class="tab profile">
      <svg width="44" height="42" viewBox="0 0 44 42"><circle cx="22" cy="11" r="10" fill="#fff"/><path d="M2 42c0-12 8-18 20-18s20 6 20 18z" fill="#fff"/></svg>
      <span>Profile</span>
    </div>
    <div class="tab home">
      <svg width="42" height="38" viewBox="0 0 42 38"><path d="M21 2L2 19h5v17h10V25h8v11h10V19h5z" fill="none" stroke="#fff" stroke-width="3" stroke-linejoin="round"/></svg>
      <span>Home</span>
    </div>
    <div class="tab more">
      <svg width="50" height="16" viewBox="0 0 50 16"><circle cx="8" cy="8" r="6" fill="#e48bbf"/><circle cx="25" cy="8" r="6" fill="#fff"/><circle cx="42" cy="8" r="6" fill="#e48bbf"/></svg>
      <span>More</span>
    </div>
  </nav>
</div>
</body>
</html>
```